43 Year Old Construction firm needs Updated Business Card & Stationery Design

We are an established and well known (in our market) commercial construction firm. We need a cleaner and more modern look for our corporate identity material. We would like to continue to use our current colors and logo.
We are thinking about incorporating a slogan on our business card (either front or back): "Striving to be the most trusted builder in our market." The text could change at some point. Our website is www.kradworth.example . Sample card is attached. Some will have more phone numbers, etc...
Updates

Target Market(s)

Commercial and institutional clients.

Industry/Entity Type

Construction Company

Contact Information for Business Card

See attached for existing card. But don't be constrained.

Requirements
Must have
• Logo, name, title, address, website, email, phone numbers (as few as one, as many as three)
• Slogan on front or back "Striving to be the most trusted builder in our market"
• Use existing logo and colors

```html
<!DOCTYPE html>
<html lang="en">
<head>
<meta charset="utf-8">
<title>Kradworth Builders — Business Card</title>
<link rel="stylesheet" href="https://fonts.googleapis.com/css2?family=Josefin+Sans:wght@400;600;700&display=swap">
<style>
  :root {
    --navy: #1b4684;
    --green: #16a05a;
    --white: #ffffff;
    --ink: #1b4684;
    --backdrop: #e9ecef;
  }
  * { box-sizing: border-box; margin: 0; padding: 0; }
  html, body { width: 1200px; height: 800px; overflow: hidden; }
  body {
    background: var(--backdrop);
    font-family: "Josefin Sans", sans-serif;
    display: flex;
    align-items: center;
    justify-content: center;
    gap: 40px;
  }
  .card {
    width: 540px;
    height: 309px;
    position: relative;
    overflow: hidden;
    box-shadow: 0 6px 18px rgba(0,0,0,0.18);
  }

  /* Front: contact panel + brand panel */
  .card-front { display: flex; background: var(--navy); }
  .contact-panel {
    width: 46%;
    background: var(--white);
    color: var(--ink);
    padding: 46px 0 0 38px;
  }
  .person-name { font-weight: 700; font-size: 18px; }
  .person-title { font-weight: 600; font-size: 15px; margin: 4px 0 0 14px; }
  .address { font-size: 12.5px; font-weight: 600; line-height: 1.45; margin: 22px 0 0 14px; }
  .contact-list { list-style: none; margin: 18px 0 0 14px; }
  .contact-list li {
    display: flex; align-items: center; gap: 8px;
    font-size: 12.5px; font-weight: 600; line-height: 1.55;
  }
  .contact-list svg { width: 14px; height: 14px; flex: none; }
  .brand-panel {
    flex: 1;
    display: flex; align-items: center; justify-content: center;
  }

  .brand-name {
    display: flex; align-items: center; gap: 10px;
    color: var(--white);
    font-weight: 700;
    text-transform: uppercase;
    letter-spacing: 1px;
  }
  .brand-mark { background: var(--green); flex: none; }
  .brand-panel .brand-name { font-size: 25px; line-height: 1.05; }
  .brand-panel .brand-mark { width: 14px; height: 14px; }

  /* Back: slogan side */
  .card-back {
    background: var(--navy);
    color: var(--white);
    padding: 78px 0 0 52px;
  }
  .card-back .brand-name { font-size: 44px; }
  .card-back .brand-mark { width: 22px; height: 22px; }
  .slogan { font-size: 15px; font-weight: 400; margin-top: 22px; }
  .social-row {
    position: absolute; left: 52px; right: 36px; bottom: 26px;
    display: flex; justify-content: space-between;
    font-size: 12px; font-weight: 600;
  }
  .social-handle { display: flex; align-items: center; gap: 6px; }
  .social-mark { width: 11px; height: 11px; background: var(--white); }
</style>
</head>
<body>

<section class="card card-front" aria-label="Business card front">
  <div class="contact-panel">
    <p class="person-name">Dale Morrow</p>
    <p class="person-title">Vice President</p>
    <p class="address">4120 Quarry Ave.<br>Fairview, MO 63000</p>
    <ul class="contact-list">
      <li>
        <svg viewBox="0 0 16 16" fill="none" stroke="currentColor" stroke-width="1.4"><rect x="2" y="2" width="12" height="12"/><path d="M5 5h2M9 5h2M5 8h2M9 8h2M5 11h2M9 11h2"/></svg>
        (555) 014-7820
      </li>
      <li>
        <svg viewBox="0 0 16 16" fill="none" stroke="currentColor" stroke-width="1.4"><rect x="4" y="1.5" width="8" height="4"/><rect x="1.5" y="5.5" width="13" height="6"/><rect x="4" y="9.5" width="8" height="5"/></svg>
        (555) 014-1354
      </li>
      <li>
        <svg viewBox="0 0 16 16" fill="currentColor"><path d="M3.5 1.5l3 3-1.6 1.6c.8 1.8 2.2 3.2 4 4l1.6-1.6 3 3-2 2C7 13 3 9 1.5 3.5z"/></svg>
        (555) 016-4532
      </li>
      <li>
        <svg viewBox="0 0 16 16" fill="none" stroke="currentColor" stroke-width="1.4"><rect x="1.5" y="3.5" width="13" height="9"/><path d="M1.5 3.5L8 9l6.5-5.5"/></svg>
        dalem@kradworth.example
      </li>
      <li>
        <svg viewBox="0 0 16 16" fill="none" stroke="currentColor" stroke-width="1.4"><circle cx="8" cy="8" r="6.5"/><path d="M1.5 8h13M8 1.5c2.5 3 2.5 10 0 13M8 1.5c-2.5 3-2.5 10 0 13"/></svg>
        www.kradworth.example
      </li>
    </ul>
  </div>
  <div class="brand-panel">
    <p class="brand-name"><span class="brand-mark"></span>Kradworth<br>Builders</p>
  </div>
</section>

<section class="card card-back" aria-label="Business card back">
  <p class="brand-name"><span class="brand-mark"></span>Kradworth</p>
  <p class="brand-name">Builders</p>
  <p class="slogan">Striving to be the most trusted builder in our market.</p>
  <div class="social-row">
    <span class="social-handle"><span class="social-mark"></span>@kradworthbuilders</span>
    <span class="social-handle"><span class="social-mark"></span>@kradworth-builders-inc</span>
  </div>
</section>

</body>
</html>
```